Electrical Contractor Company Profile

We need a Brochure that is more entertaining than our current Company Profile Document. We have lots of great experience and awesome looking jobs in our portfolio but need a document that we can either print of send in electronic format to accompany some of our submissions.

We are ideally looking for something 9-10 pages in A4 with some of the pages opening out to A3.

We are looking for a document that is professional and smart however shows the colour and quality that we feel we offer to prospective clientele.

I have included the current Company Profile and Logo along with a number of images of completed projects that may be of use.

Target Market(s)

Builders, Facility Managers, Engineers, Decision makers

Industry/Entity Type

Electrical

Font styles to use
Sans Serif

Colors

Designer to choose colors to be used in the design.

Requirements
Must have
• - Modern look with a focus on sustainability
• - Clean Simple and Professional
• - Incorporate our Logo
• Core Business Lines need to be across an A3 opening page and have photos relating to these lines Solar, Communications and any of the projects.
Nice to have
• Lots of colour and photos mixed with the text
Should not have
• Lightning bolts or corny symbols

```html
<!DOCTYPE html>
<html lang="en">
<head>
<meta charset="utf-8">
<title>Company Profile – Core Business Spread</title>
<link href="https://fonts.googleapis.com/css2?family=Open+Sans:wght@400;600;700;800&display=swap" rel="stylesheet">
<style>
  :root{
    --bg:#2b2b2d;
    --paper:#ffffff;
    --navy:#1f3f7a;
    --ink:#2b4a86;
    --orange:#e2661b;
    --photo-a:#3a3128;
    --photo-b:#b89a5a;
    --photo-c:#6d5f52;
  }
  *{box-sizing:border-box;margin:0;padding:0}
  html,body{width:1200px;height:789px;overflow:hidden;background:var(--bg);font-family:"Open Sans",Arial,sans-serif;color:var(--ink)}
  .spread{position:absolute;left:77px;top:24px;width:1046px;height:740px;display:flex;box-shadow:0 10px 30px rgba(0,0,0,.5)}
  .page{position:relative;width:523px;height:740px;background:var(--paper);overflow:hidden}
  .page--left{border-right:1px solid #e6e6ea}
  .intro{position:absolute;left:36px;top:36px;right:36px;font-size:10.5px;line-height:1.45}
  .intro p+p{margin-top:8px}
  .col{position:absolute;left:36px;top:138px;width:200px;font-size:9.5px;line-height:1.4}
  .ticks{list-style:none;margin:0 0 10px}
  .ticks li{position:relative;padding-left:14px;margin-bottom:2px}
  .ticks li::before{content:"";position:absolute;left:1px;top:3px;width:7px;height:4px;border-left:2px solid var(--orange);border-bottom:2px solid var(--orange);transform:rotate(-45deg)}
  .lead{font-weight:700;margin:4px 0 6px}
  .photo{position:absolute;left:250px;top:150px;width:273px;height:410px;background:linear-gradient(160deg,var(--photo-a) 0%,var(--photo-c) 45%,var(--photo-b) 100%)}
  .closing{position:absolute;left:36px;top:568px;width:450px;font-size:9.5px;line-height:1.45}
  .closing p+p{margin-top:6px}
  .brand{position:absolute;left:36px;display:flex;align-items:center;gap:8px;font-weight:800;font-size:20px;color:var(--navy);letter-spacing:.5px}
  .brand__dot{width:22px;height:22px;border-radius:50%;background:var(--orange)}
  .page--left .brand{top:650px}
  .web-bar{position:absolute;height:28px;background:var(--orange);color:#fff;font-size:12px;font-weight:600;display:flex;align-items:center;justify-content:flex-end;padding-right:24px;gap:8px}
  .page--left .web-bar{left:250px;right:0;top:690px}
  .page--right .web-bar{left:230px;right:0;top:690px;justify-content:center}
  .tab{position:absolute;left:36px;top:30px;background:var(--orange);color:#fff;font-size:14px;font-weight:600;padding:7px 16px;letter-spacing:.5px}
  .headline{position:absolute;left:36px;top:72px;right:30px;font-size:14px;font-weight:600;color:var(--navy)}
  .lines{position:absolute;left:36px;top:104px;right:30px;list-style:none}
  .line{margin-bottom:12px}
  .line__bar{display:flex;align-items:center;width:240px;height:22px;background:var(--navy);color:#fff;font-size:11px;font-weight:600}
  .line__num{width:18px;height:22px;background:var(--orange);display:flex;align-items:center;justify-content:center;font-weight:700;margin-right:10px}
  .line__text{font-size:8.6px;line-height:1.4;margin-top:5px}
  .page--right .brand{top:650px}
</style>
</head>
<body>
<div class="spread">
  <section class="page page--left">
    <div class="intro">
      <p>Established in 2006, Meridian Electrical Services is an award winning business offering expertise across a diverse range of electrical services including commercial, industrial and communications.</p>
      <p>Meridian has the experience and capability to complete contracts for large and small along with a focus on private organizations and government agencies. Our services include:</p>
    </div>
    <div class="col">
      <ul class="ticks">
        <li>Electrical projects;</li>
        <li>Planned and reactive maintenance;</li>
        <li>Design and construct;</li>
        <li>Electrical Drafting;</li>
        <li>Communications;</li>
        <li>Minor works;</li>
        <li>Solar power generation and storage;</li>
        <li>Electronic lighting control;</li>
      </ul>
      <p class="lead">Meridian Electrical enjoys a high volume of repeat business, which is a result of our:</p>
      <ul class="ticks">
        <li>Commitment to consistently achieving quality results;</li>
        <li>Priority of dealing openly with our clients, staff and suppliers to begin and maintain honest, open and positive relationships;</li>
        <li>Innovation and ability to effectively source and utilize new and emerging technologies;</li>
        <li>Knowledgeable and experienced staff who have the ability to complete a range of complex projects;</li>
        <li>Team's ability to develop designs and work systems to meet site requirements and prevent project delays; and</li>
        <li>Proven approach to project management.</li>
      </ul>
    </div>
    <div class="photo" role="img" aria-label="Photo of a completed retail arcade fit-out with feature lighting and a colourful mural"></div>
    <div class="closing">
      <p>Our ability to deliver successful projects was recognized at both the 2015 &amp; 2016 State Electrical Excellence Awards, in which we received awards in the Best Lighting and Best Commercial Project &lt;1M Category's.</p>
      <p>With an office and warehouse situated centrally in East Harbour, Meridian Electrical Services is well placed to service the broader metropolitan area and regional areas throughout the state.</p>
    </div>
    <div class="brand"><span class="brand__dot"></span>MERIDIAN ELECTRICAL</div>
    <div class="web-bar">
      <svg width="12" height="12" viewBox="0 0 12 12" aria-hidden="true"><circle cx="6" cy="6" r="5" fill="none" stroke="#fff" stroke-width="1.2"/><path d="M1 6h10M6 1c2 2 2 8 0 10M6 1c-2 2-2 8 0 10" fill="none" stroke="#fff" stroke-width="1"/></svg>
      www.meridianelectrical.example
    </div>
  </section>

  <section class="page page--right">
    <div class="tab">CORE BUSINESS</div>
    <h2 class="headline">Meridian Electrical Services maintains five core lines of business:</h2>
    <ol class="lines">
      <li class="line">
        <div class="line__bar"><span class="line__num">1</span>Breakdown and response</div>
        <p class="line__text">Providing a 24/7 call out service to a number of high profile clients this team is high energy and responsive to most situations. Consistently performing at the top level of our clients expectations have resulted in excellent growth in this sector.</p>
      </li>
      <li class="line">
        <div class="line__bar"><span class="line__num">2</span>Planned Maintenance</div>
        <p class="line__text">This team service over 500 sites across the Harbour City metropolitan area. Carrying out planned testing and repair of all electrical infrastructure required by our clients. This includes RCD and Emergency lighting along with thermographic surveys amongst many other services.</p>
      </li>
      <li class="line">
        <div class="line__bar"><span class="line__num">3</span>Electrical Projects</div>
        <p class="line__text">This line of business is responsible for completing contracts both considered minor and major in value. Team members are experienced in installing various types of electrical systems and are well equipped in producing the high quality workmanship expected in this highly competitive sector.</p>
      </li>
      <li class="line">
        <div class="line__bar"><span class="line__num">4</span>Communications</div>
        <p class="line__text">Our staff are extremely experienced and the majority carry Open Cabling licenses &amp; Certificate III qualifications in Telecommunications. The company own substantial amounts of specialized test equipment and regularly invest in continued training of staff. MES can supply both design and installation services for private networks. Providing a certified solution to any copper and fiber optic needs.</p>
      </li>
      <li class="line">
        <div class="line__bar"><span class="line__num">5</span>Solar PV</div>
        <p class="line__text">Focusing on the commercial market we are able to offer fully design solutions for photovoltaic systems up to 200KW designed to suit a client's needs and budgets. With highly trained and experienced consultants and installers we pride ourselves on offering great value for money and clarity on project benefits.</p>
      </li>
      <li class="line">
        <div class="line__bar"><span class="line__num">6</span>Technology Services</div>
        <p class="line__text">With great base knowledge and an ongoing commitment to training and innovation, MES are able to offer solutions for Energy Management, Energy Conservation, Electronic Lighting Control, Premises performance auditing and Power monitoring. Providing our clients with valuable expertise in reduction of running costs and better understanding of their assets maintenance requirements, producing ongoing savings in operation and replacement of plant.</p>
      </li>
    </ol>
    <div class="brand"><span class="brand__dot"></span>MERIDIAN ELECTRICAL</div>
    <div class="web-bar">
      <svg width="12" height="12" viewBox="0 0 12 12" aria-hidden="true"><circle cx="6" cy="6" r="5" fill="none" stroke="#fff" stroke-width="1.2"/><path d="M1 6h10M6 1c2 2 2 8 0 10M6 1c-2 2-2 8 0 10" fill="none" stroke="#fff" stroke-width="1"/></svg>
      www.meridianelectrical.example
    </div>
  </section>
</div>
</body>
</html>
```